依頼詳細
今年の仮チラシをファイル添付しておきますので、講師の肩書、名前等の確認をお願いいたします。

昨年の講演会のチラシもファイル添付しておきますので、参考にお願いいたします。

こどもさんの笑顔の写真や、家族で幸せそうにしている写真がありそうでしたら、多めに使用していただけますか。
記載項目
記載項目は基本2018年のチラシと同じですので、ファイル添付分で確認をおねがいします。(日付だけが、9月21日(土)となります。)
サイズ
A4
ページ数
片面
希望イメージ
シンプル 複雑
単色 カラフル
暗い 明るい
日常 高級
遊び心 厳粛
未来的 伝統的
女性的 男性的
希望する色
水色系、緑系、黄・オレンジ系
納品ファイル
• 高解像度JPG (.jpg)
補足説明
今年の講演会チラシにも講師二人の写真を入れる予定です。撮影できしだいファイルをおくるかたちとなります。よろしくお願いいたします。
■ 選んだ理由

イメージと合ったから。

■ 提案者全員のお礼・コメント

みなさん、ご協力ありがとうございました。

```html
<!DOCTYPE html>
<html lang="ja">
<head>
<meta charset="utf-8">
<title>こどもの栄養・こどもの姿勢 講演会</title>
<link href="https://fonts.googleapis.com/css2?family=M+PLUS+Rounded+1c:wght@500;800;900&family=Noto+Sans+JP:wght@400;500;700;900&display=swap" rel="stylesheet">
<style>
  :root {
    --orange: #f39a1e;
    --orange-deep: #ea7a12;
    --green: #7cbf2f;
    --green-deep: #4f9a22;
    --red: #e2231a;
    --ink: #3a3a3a;
    --muted: #777;
    --sky: #d8ecf6;
    --paper: #ffffff;
  }
  * { margin: 0; padding: 0; box-sizing: border-box; }
  html, body { width: 846px; height: 1200px; overflow: hidden; background: var(--paper); }
  body { font-family: "Noto Sans JP", sans-serif; color: var(--ink); }
  .flyer { position: relative; width: 846px; height: 1200px; overflow: hidden; background: var(--paper); }

  .hero-photo {
    position: absolute; left: 0; top: 0; width: 846px; height: 600px;
    background: linear-gradient(160deg, #eef6fb 0%, #f7e9dc 40%, #e9f1e0 70%, #f4f0e8 100%);
  }
  .hero-fade {
    position: absolute; left: 0; top: 430px; width: 846px; height: 170px;
    background: linear-gradient(to bottom, rgba(255,255,255,0) 0%, rgba(255,255,255,.9) 60%, #fff 100%);
  }

  .tagline {
    position: absolute; left: 268px; top: 16px; width: 352px; height: 110px;
    border-radius: 55px; background: rgba(255,255,255,.88);
    border: 3px solid var(--green);
    display: flex; flex-direction: column; align-items: center; justify-content: center;
    font-family: "M PLUS Rounded 1c", sans-serif; font-weight: 800; color: var(--green-deep);
    line-height: 1.25;
  }
  .tagline .line1 { font-size: 26px; }
  .tagline .line2 { font-size: 30px; }

  .theme-ovals { position: absolute; left: 120px; top: 190px; width: 626px; height: 270px; }
  .oval {
    position: absolute; top: 0; width: 322px; height: 262px; border-radius: 50%;
    display: flex; flex-direction: column; align-items: center; justify-content: center;
    font-family: "M PLUS Rounded 1c", sans-serif; font-weight: 900; color: #fff;
    text-shadow: 0 2px 3px rgba(0,0,0,.15);
    box-shadow: 0 4px 10px rgba(0,0,0,.12);
  }
  .oval .small { font-size: 48px; line-height: 1.1; }
  .oval .large { font-size: 72px; line-height: 1.15; letter-spacing: 2px; }
  .oval-nutrition { left: 0; background: radial-gradient(circle at 40% 35%, #ffb54a, var(--orange-deep)); }
  .oval-posture { left: 300px; background: radial-gradient(circle at 55% 35%, #9fd65a, var(--green-deep)); mix-blend-mode: normal; opacity: .97; }

  .lead {
    position: absolute; left: 40px; top: 470px; width: 766px;
    text-align: center; color: var(--red); font-weight: 700; font-size: 15.5px; line-height: 1.6;
  }

  .speakers { position: absolute; left: 0; top: 580px; width: 846px; height: 270px; }
  .speaker { position: absolute; top: 0; width: 380px; height: 260px; }
  .speaker-left { left: 60px; }
  .speaker-right { left: 450px; }
  .speaker-role { font-size: 13px; font-weight: 700; color: var(--ink); }
  .speaker-name { margin-top: 2px; font-size: 26px; font-weight: 900; color: var(--ink); letter-spacing: 2px; }
  .speaker-name .honorific { font-size: 15px; font-weight: 500; margin-left: 4px; }
  .speaker-bio { margin-top: 14px; width: 228px; font-size: 12px; line-height: 1.65; color: var(--ink); }
  .speaker-photo {
    position: absolute; right: 10px; top: 50px; width: 124px; height: 124px; border-radius: 50%;
    background: linear-gradient(150deg, #c9c9c9, #a8a8a8);
  }

  .divider { position: absolute; left: 40px; top: 868px; width: 766px; height: 2px; background: var(--orange); }

  .event-info { position: absolute; left: 50px; top: 880px; width: 470px; }
  .era { font-size: 15px; font-weight: 700; color: var(--ink); }
  .date-row { display: flex; align-items: flex-end; gap: 14px; margin-top: -4px; }
  .date { font-family: "M PLUS Rounded 1c", sans-serif; font-weight: 900; color: var(--red); font-size: 88px; line-height: 1; letter-spacing: -2px; }
  .weekday {
    display: inline-flex; align-items: center; justify-content: center;
    width: 34px; height: 34px; border-radius: 50%; background: var(--red); color: #fff;
    font-size: 19px; font-weight: 900; margin-left: 4px; vertical-align: 10px; letter-spacing: 0;
  }
  .times { padding-bottom: 8px; }
  .time-main { font-size: 22px; font-weight: 900; color: var(--red); }
  .time-main .label { font-size: 16px; }
  .time-sub { font-size: 14px; font-weight: 700; color: var(--red); }
  .fee { margin-top: 12px; font-size: 25px; font-weight: 900; color: var(--red); }
  .fee .note { font-size: 11px; font-weight: 500; color: var(--ink); margin-left: 8px; }
  .venue { margin-top: 6px; font-size: 22px; font-weight: 900; color: var(--ink); }
  .address { margin-top: 4px; font-size: 12.5px; color: var(--ink); line-height: 1.5; }

  .access-map {
    position: absolute; left: 530px; top: 880px; width: 288px; height: 232px;
    background: linear-gradient(135deg, #f3f3f3, #e4e4e4);
    border: 1px solid #cfcfcf;
  }

  .organizer { position: absolute; left: 50px; top: 1138px; width: 760px; }
  .organizer-name { font-size: 17px; font-weight: 900; color: var(--ink); }
  .organizer-contact { font-size: 11.5px; color: var(--muted); margin-top: 2px; }
</style>
</head>
<body>
<div class="flyer">
  <div class="hero-photo" role="img" aria-label="笑顔のこどもたちと食卓を囲む幸せそうな家族の写真コラージュ"></div>
  <div class="hero-fade"></div>

  <div class="tagline">
    <span class="line1">こどもたちの</span>
    <span class="line2">輝かしい未来のために!</span>
  </div>

  <div class="theme-ovals">
    <div class="oval oval-nutrition"><span class="small">こどもの</span><span class="large">栄養</span></div>
    <div class="oval oval-posture"><span class="small">こどもの</span><span class="large">姿勢</span></div>
  </div>

  <p class="lead">
    平成17年に食育基本法が制定されて以来、長年学校教育で児童の栄養指導を行ってきた<br>
    こどもの栄養専門家と大学で姿勢の専門家を育ててきた博士(健康科学)によるコラボレーション講演会
  </p>

  <section class="speakers">
    <div class="speaker speaker-left">
      <p class="speaker-role">管理栄養士</p>
      <p class="speaker-name">山野 彩香<span class="honorific">氏</span></p>
      <p class="speaker-bio">学校給食に携わりアレルギー対策、成長期の食事などを中心に、こどもたちの食と健康を長く支えてきた。バランスの良い食事が成長に与える影響について、家庭ですぐ実践できる工夫をわかりやすく伝えています。</p>
      <div class="speaker-photo" role="img" aria-label="講師 山野 彩香氏の写真"></div>
    </div>
    <div class="speaker speaker-right">
      <p class="speaker-role">健康科学博士</p>
      <p class="speaker-name">川辺 浩一<span class="honorific">氏</span></p>
      <p class="speaker-bio">こどもの姿勢が心と体の成長に与える影響を研究し、大学で後進の育成に力を注ぐ。日々の座り方や立ち方を見直すことで、集中力や健やかな発育につながる方法を紹介しています。</p>
      <div class="speaker-photo" role="img" aria-label="講師 川辺 浩一氏の写真"></div>
    </div>
  </section>

  <div class="divider"></div>

  <section class="event-info">
    <p class="era">令和元年</p>
    <div class="date-row">
      <p class="date">9/21<span class="weekday">土</span></p>
      <div class="times">
        <p class="time-main"><span class="label">開演</span>/13:30</p>
        <p class="time-sub">(開場/13:00)</p>
      </div>
    </div>
    <p class="fee">参加費/4,000円<span class="note">※当日受付にてお支払いください</span></p>
    <p class="venue">会 場/まなびプラザ中央 2階ホール</p>
    <p class="address">〒600-0000 みやこ市中央区まなび通一丁目12番地</p>
  </section>

  <div class="access-map" role="img" aria-label="会場までのアクセス地図"></div>

  <footer class="organizer">
    <p class="organizer-name">主催/みやこ姿勢調整協会</p>
    <p class="organizer-contact">〒600-0001 みやこ市中央区さくら町3-4　TEL 000-123-4567　FAX 000-123-4568</p>
  </footer>
</div>
</body>
</html>
```